Kestrel Photography Business Card

I need a business card designed for a photography business based in Perth, Western Australia called Kestrel Photography.

We specialise in wedding, event photography and portrait photography.

The business card must borrow the style of the attached logo.

The hex codes for the colours in the logo are:
#ED1D85 - Pink
#89C23E - Green
#37282F - Black

The name on the card will be:
Name: Toviran
Phone: 0417395268
Website: www.kestrelphotography.com.au
Facebook: kestrelphotography

I am open and happy to accept creative concepts.

I’d like some space at the back for writing notes and appointment details.

```html
<!DOCTYPE html>
<html lang="en">
<head>
<meta charset="utf-8">
<title>Kestrel Photography – Business Card</title>
<link rel="stylesheet" href="https://fonts.googleapis.com/css2?family=Montserrat:wght@300&family=Dawning+of+a+New+Day&family=Cutive+Mono&display=swap">
<style>
  :root {
    --pink: #ED1D85;
    --green: #89C23E;
    --ink: #37282F;
    --paper: #FFFFFF;
    --backdrop: #CDE0CE;
  }
  * { margin: 0; padding: 0; box-sizing: border-box; }
  html, body { width: 1200px; height: 848px; overflow: hidden; }
  body {
    background: var(--backdrop);
    display: flex;
    align-items: center;
    justify-content: center;
    gap: 60px;
  }
  .card {
    width: 500px;
    height: 286px;
    background: var(--paper);
    position: relative;
    box-shadow: 0 2px 6px rgba(55, 40, 47, 0.12);
  }

  /* Front */
  .card-front {
    display: flex;
    flex-direction: column;
    align-items: center;
    justify-content: center;
    gap: 26px;
  }
  .brand-dot {
    width: 118px;
    height: 118px;
    border-radius: 50%;
    background: var(--pink);
  }
  .brand-name {
    font-family: "Montserrat", sans-serif;
    font-weight: 300;
    font-size: 15px;
    letter-spacing: 0.42em;
    text-transform: uppercase;
    color: var(--ink);
    padding-left: 0.42em;
  }

  /* Back */
  .card-back {
    border: 9px solid var(--pink);
    padding: 30px 34px;
    color: var(--ink);
  }
  .holder-name {
    font-family: "Dawning of a New Day", cursive;
    font-size: 46px;
    line-height: 1;
    margin-left: 70px;
  }
  .phone {
    display: flex;
    align-items: center;
    gap: 10px;
    margin: 10px 0 0 56px;
    font-family: "Dawning of a New Day", cursive;
    font-size: 34px;
    line-height: 1;
  }
  .phone svg { width: 18px; height: 18px; fill: var(--ink); }
  .contact-lines {
    position: absolute;
    left: 34px;
    bottom: 28px;
    font-family: "Cutive Mono", monospace;
    font-size: 13px;
    line-height: 1.7;
  }
  .social {
    display: flex;
    align-items: center;
    gap: 7px;
  }
  .social-square {
    width: 11px;
    height: 11px;
    background: var(--ink);
  }
</style>
</head>
<body>
  <section class="card card-front" aria-label="Business card front">
    <div class="brand-dot"></div>
    <p class="brand-name">Kestrel Photography</p>
  </section>

  <section class="card card-back" aria-label="Business card back">
    <p class="holder-name">Toviran</p>
    <p class="phone">
      <svg viewBox="0 0 24 24" aria-hidden="true"><path d="M6.6 10.8a15.1 15.1 0 0 0 6.6 6.6l2.2-2.2c.3-.3.7-.4 1-.2 1.1.4 2.3.6 3.6.6.6 0 1 .4 1 1V20c0 .6-.4 1-1 1A17 17 0 0 1 3 4c0-.6.4-1 1-1h3.5c.6 0 1 .4 1 1 0 1.3.2 2.5.6 3.6.1.3 0 .7-.2 1z"/></svg>
      0417395268
    </p>
    <div class="contact-lines">
      <p class="social"><span class="social-square"></span>kestrelphotography</p>
      <p class="website">www.kestrelphotography.com.au</p>
    </div>
  </section>
</body>
</html>
```